Packiging of mouse trap

We need a packiging for a new mousetrap called 'The Snapwell'. It is a mouse/rat trap. We want to have it pretty simple and modern. The logo of the mouse trap is in the attachment and the measures of the packaging also (don't look at the design, it has nothing to do with us). It's needs to stand out in between the other packaging due to it's simplicity and modern touch.

Font styles to use
Sans Serif

Requirements
Must have
• Simplicity, modern
Should not have
• Too many colors

```html
<!DOCTYPE html>
<html lang="en">
<head>
<meta charset="UTF-8">
<title>The Snapwell – Electric Mouse Trap Packaging</title>
<link href="https://fonts.googleapis.com/css2?family=Exo+2:wght@300;400;600;800&display=swap" rel="stylesheet">
<style>
  :root{
    --stage:#d9d9d9;
    --paper:#f7f7f7;
    --pattern:#efefef;
    --logo-grey:#c9c9c9;
    --ink:#1c1d1e;
    --white:#ffffff;
    --green:#6cbf4b;
    --rule:#bfbfbf;
  }
  *{margin:0;padding:0;box-sizing:border-box}
  html,body{width:1200px;height:960px;overflow:hidden}
  body{
    background:radial-gradient(circle at 40% 45%, #ececec 0%, var(--stage) 70%);
    font-family:"Exo 2", sans-serif;
    display:flex;align-items:center;justify-content:center;
  }
  .dieline{display:flex;height:880px;box-shadow:0 18px 40px rgba(0,0,0,.18)}
  .panel{position:relative;display:flex;flex-direction:column;overflow:hidden}
  .panel--side{width:230px;border-right:1px solid #dcdcdc}
  .panel--front{width:360px}
  .panel__upper{position:relative;flex:0 0 62%;background:var(--paper)}
  .panel__pattern{
    position:absolute;inset:0;
    background:linear-gradient(135deg,var(--paper) 0%,var(--pattern) 50%,var(--paper) 100%);
  }
  .badge{
    position:absolute;top:0;background:var(--green);color:var(--white);
    text-align:center;font-weight:600;
    clip-path:polygon(0 0,100% 0,100% 100%,50% 82%,0 100%);
  }
  .panel--front .badge{left:44px;width:94px;height:104px;padding-top:12px;font-size:13px;line-height:1.2}
  .panel--side .badge{left:22px;width:62px;height:82px;padding-top:8px;font-size:9px;line-height:1.2;font-weight:400}
  .badge__rule{display:block;width:70%;height:1px;background:var(--white);margin:5px auto}
  .brand{
    position:absolute;left:0;right:0;text-align:center;color:var(--logo-grey);
    font-weight:800;text-transform:uppercase;line-height:.95;
  }
  .panel--front .brand{bottom:70px;font-size:58px}
  .panel--side .brand{bottom:50px;font-size:38px}
  .panel__lower{flex:1;background:var(--ink);color:var(--white);text-align:center;display:flex;flex-direction:column;align-items:center}
  .title{font-weight:300;text-transform:uppercase;letter-spacing:.02em;line-height:1.7}
  .panel--front .title{font-size:25px;margin-top:50px}
  .panel--side .title{font-size:17px;margin-top:40px}
  .features{display:grid;grid-template-columns:1fr 1fr;margin-top:22px}
  .feature{display:flex;align-items:center;gap:7px;font-weight:400;color:#e6e6e6}
  .panel--front .feature{font-size:12px;padding:9px 12px}
  .panel--side .feature{font-size:9px;padding:6px 7px}
  .feature:nth-child(1),.feature:nth-child(3){border-right:1px solid var(--rule)}
  .feature:nth-child(1),.feature:nth-child(2){border-bottom:1px solid var(--rule)}
  .feature svg{flex:none}
  .site{margin-top:auto;margin-bottom:50px;font-weight:400;letter-spacing:.03em}
  .panel--front .site{font-size:11px}
  .panel--side .site{font-size:8px}
</style>
</head>
<body>
  <main class="dieline">
    <section class="panel panel--side">
      <div class="panel__upper">
        <div class="panel__pattern" role="img" aria-label="Faint circuit-line pattern with small mouse silhouettes"></div>
        <div class="badge">INSTANT<br>KILL TRAP<span class="badge__rule"></span>PET SAFE</div>
        <div class="brand">The<br>Snapwell</div>
      </div>
      <div class="panel__lower">
        <h2 class="title">Electric<br>Mouse Trap</h2>
        <ul class="features">
          <li class="feature"><svg width="12" height="12" viewBox="0 0 20 20"><circle cx="10" cy="10" r="8.5" fill="none" stroke="#fff" stroke-width="1.5"/><path d="M6 10l3 3 5-6" fill="none" stroke="#fff" stroke-width="1.6"/></svg>Easy to use</li>
          <li class="feature"><svg width="12" height="12" viewBox="0 0 20 20"><circle cx="10" cy="10" r="8.5" fill="none" stroke="#fff" stroke-width="1.5"/><path d="M6 10a4 4 0 0 1 7-2.6M14 10a4 4 0 0 1-7 2.6" fill="none" stroke="#fff" stroke-width="1.5"/></svg>Reusable</li>
          <li class="feature"><svg width="12" height="12" viewBox="0 0 20 20"><circle cx="10" cy="10" r="8.5" fill="none" stroke="#fff" stroke-width="1.5"/><path d="M6 10h8" stroke="#fff" stroke-width="1.6"/></svg>No Injuries</li>
          <li class="feature"><svg width="12" height="12" viewBox="0 0 20 20"><circle cx="10" cy="10" r="8.5" fill="none" stroke="#fff" stroke-width="1.5"/><path d="M11 4l-4 7h4l-2 5 5-7h-4z" fill="#fff"/></svg>Powerful</li>
        </ul>
        <p class="site">WWW.SNAPWELLTRAP.COM</p>
      </div>
    </section>

    <section class="panel panel--front">
      <div class="panel__upper">
        <div class="panel__pattern" role="img" aria-label="Faint circuit-line pattern with small mouse silhouettes"></div>
        <div class="badge">INSTANT<br>KILL TRAP<span class="badge__rule"></span>PET SAFE</div>
        <div class="brand">The<br>Snapwell</div>
      </div>
      <div class="panel__lower">
        <h1 class="title">Electric<br>Mouse Trap</h1>
        <ul class="features">
          <li class="feature"><svg width="18" height="18" viewBox="0 0 20 20"><circle cx="10" cy="10" r="8.5" fill="none" stroke="#fff" stroke-width="1.5"/><path d="M6 10l3 3 5-6" fill="none" stroke="#fff" stroke-width="1.6"/></svg>Easy to use</li>
          <li class="feature"><svg width="18" height="18" viewBox="0 0 20 20"><circle cx="10" cy="10" r="8.5" fill="none" stroke="#fff" stroke-width="1.5"/><path d="M6 10a4 4 0 0 1 7-2.6M14 10a4 4 0 0 1-7 2.6" fill="none" stroke="#fff" stroke-width="1.5"/></svg>Reusable</li>
          <li class="feature"><svg width="18" height="18" viewBox="0 0 20 20"><circle cx="10" cy="10" r="8.5" fill="none" stroke="#fff" stroke-width="1.5"/><path d="M6 10h8" stroke="#fff" stroke-width="1.6"/></svg>No Injuries</li>
          <li class="feature"><svg width="18" height="18" viewBox="0 0 20 20"><circle cx="10" cy="10" r="8.5" fill="none" stroke="#fff" stroke-width="1.5"/><path d="M11 4l-4 7h4l-2 5 5-7h-4z" fill="#fff"/></svg>Powerful</li>
        </ul>
        <p class="site">WWW.SNAPWELLTRAP.COM</p>
      </div>
    </section>
  </main>
</body>
</html>
```